CREST Academy Exhibit Booth Posters

My company is CREST Academy (a division of CREST for Growth). We are exhibiting in a month, and I need to re-do my exhibit booth posters. There will be a total of 4 posters needed. Sizes are below.
1) Top- 11 feet long X 12 inches wide (Try to match color scheme in example photo)
2) Center- 4 feet long X 2 feet wide (Chalkboard background)
3) Left- 18 inches long X 2 feet wide (Cork-board back ground with the use of push pins holding up post-it-notes, paper, etc.)
4) Right- 18 inches long X 2 feet wide (Cork-board back ground with the use of push pins holding up post-it-notes, paper, etc.)
I have attached a photo of my old booth. This will get you an idea of the size, color schemes, and more. I have created basic rendering of each poster. The content is important, but the look and design should be drastically improved.
The websites to look into for ideas are:
www.crestforgrowth.example
www.crestacademy.example
Updates
I've added a new file. It's a .JPG of the certification diploma. Thanks!
Target Market(s)
Business Owners, Managers, HR, Supervisors, Teens who want to boost their resume
Industry/Entity Type
It Company
Look and feel

```html
<!DOCTYPE html>
<html lang="en">
<head>
<meta charset="utf-8">
<title>CREST Academy — Get Your Employees Certified</title>
<link rel="stylesheet" href="https://fonts.googleapis.com/css2?family=Oswald:wght@700&family=UnifrakturMaguntia&family=Pinyon+Script&family=Gochi+Hand&family=Open+Sans:wght@400;600&display=swap">
<style>
  :root {
    --wood-dark: #7a3e14;
    --wood: #b5642a;
    --wood-light: #d08745;
    --cork: #c08a55;
    --cork-dark: #a8723f;
    --paper: #ebe8da;
    --tape: rgba(230, 220, 90, 0.75);
    --ink: #111111;
    --cert-white: #ffffff;
    --cert-gold: #c9a64a;
    --cert-silver: #b9b9b9;
    --pin-red: #c8121a;
    --sticky: #f4f05a;
    --sticky-edge: #e2dc3c;
    --lined: #f6f6f2;
    --line-blue: #a9c3dd;
    --margin-red: #e4a0a0;
    --marker-red: #d9141c;
    --photo-frame: #f2f2f2;
  }
  * { box-sizing: border-box; margin: 0; padding: 0; }
  html, body { width: 900px; height: 1200px; overflow: hidden; background: #ffffff; }

  .poster {
    position: relative;
    width: 900px;
    height: 1200px;
    background: linear-gradient(135deg, var(--wood-light), var(--wood) 45%, var(--wood-dark));
    overflow: hidden;
  }
  .cork {
    position: absolute;
    left: 34px; top: 34px; right: 34px; bottom: 34px;
    background: radial-gradient(ellipse at 40% 35%, var(--cork), var(--cork-dark));
    box-shadow: inset 0 0 18px rgba(60, 25, 5, 0.6);
  }

  /* Headline note */
  .headline-note {
    position: absolute;
    left: 60px; top: 52px;
    width: 770px; height: 290px;
    background: var(--paper);
    transform: rotate(2.2deg);
    box-shadow: 4px 6px 12px rgba(0,0,0,0.35);
    display: flex; flex-direction: column; align-items: center; justify-content: center;
  }
  .headline {
    font-family: "Oswald", sans-serif;
    font-weight: 700;
    color: var(--ink);
    text-align: center;
    line-height: 1.2;
    font-size: 74px;
    letter-spacing: 3px;
    text-transform: uppercase;
  }
  .tape {
    position: absolute;
    width: 110px; height: 48px;
    background: var(--tape);
  }
  .tape--tl { left: -22px; top: 14px; transform: rotate(-40deg); }
  .tape--tr { right: -30px; top: 8px; transform: rotate(48deg); }
  .tape--bl { left: -26px; bottom: 30px; transform: rotate(38deg); }
  .tape--br { right: -30px; bottom: 22px; transform: rotate(-42deg); }

  /* Certificate */
  .certificate {
    position: absolute;
    left: 163px; top: 345px;
    width: 600px; height: 420px;
    background: var(--cert-white);
    box-shadow: 3px 5px 10px rgba(0,0,0,0.35);
    padding: 12px;
  }
  .certificate__frame {
    width: 100%; height: 100%;
    border: 10px solid var(--cert-gold);
    outline: 4px solid var(--cert-silver);
    outline-offset: -18px;
    position: relative;
    text-align: center;
    padding: 30px 40px 0;
    font-family: "Open Sans", sans-serif;
    color: var(--ink);
  }
  .certificate__school { font-family: "UnifrakturMaguntia", serif; font-size: 19px; }
  .certificate__title { font-family: "UnifrakturMaguntia", serif; font-size: 23px; margin-top: 10px; }
  .certificate__name {
    font-family: "Pinyon Script", cursive;
    font-size: 24px;
    margin: 6px 30px 0;
    padding-bottom: 2px;
    border-bottom: 1px solid #333;
  }
  .certificate__body { font-size: 7.4px; line-height: 1.9; margin-top: 14px; }
  .certificate__body--main { margin-top: 0; }
  .certificate__course { font-family: "UnifrakturMaguntia", serif; font-size: 18px; margin: 2px 0; }
  .certificate__seal {
    position: absolute;
    left: 255px; top: 268px;
    width: 56px; height: 56px;
    border-radius: 50%;
    background: radial-gradient(circle, #f2c94c, #c99a1f);
  }
  .certificate__date {
    position: absolute;
    left: 350px; top: 313px;
    width: 150px;
    border-top: 1px solid #333;
    font-size: 9px;
    padding-top: 3px;
  }

  .pin {
    position: absolute;
    width: 24px; height: 24px;
    border-radius: 50%;
    background: radial-gradient(circle at 35% 35%, #ff5a5a, var(--pin-red) 60%, #7a0508);
    box-shadow: 2px 3px 4px rgba(0,0,0,0.45);
    z-index: 5;
  }

  /* Photo print */
  .photo-print {
    position: absolute;
    left: 95px; top: 618px;
    width: 345px; height: 262px;
    background: var(--photo-frame);
    padding: 12px 12px 30px;
    transform: rotate(-0.8deg);
    box-shadow: 3px 5px 10px rgba(0,0,0,0.4);
  }
  .photo-print__image {
    width: 100%; height: 100%;
    background: linear-gradient(160deg, #5a4a44, #7a4a3a 45%, #2e2a2e);
  }

  /* Sticky note */
  .sticky-note {
    position: absolute;
    left: 510px; top: 735px;
    width: 340px; height: 215px;
    background: linear-gradient(170deg, var(--sticky), var(--sticky-edge));
    transform: rotate(-3deg);
    box-shadow: 4px 6px 10px rgba(0,0,0,0.35);
    display: flex; align-items: center; justify-content: center;
  }
  .sticky-note__text {
    font-family: "Gochi Hand", cursive;
    font-size: 48px;
    line-height: 1.22;
    text-align: center;
    color: var(--ink);
    transform: rotate(-7deg);
  }

  /* Lined paper */
  .lined-paper {
    position: absolute;
    left: 58px; top: 872px;
    width: 520px; height: 280px;
    transform: rotate(-1.2deg);
    filter: drop-shadow(3px 5px 6px rgba(0,0,0,0.35));
  }
  .lined-paper svg { position: absolute; inset: 0; }
  .lined-paper__text {
    position: absolute;
    left: 30px; right: 0; top: 16px;
    font-family: "Gochi Hand", cursive;
    font-size: 64px;
    line-height: 1.22;
    text-align: center;
    color: var(--marker-red);
    letter-spacing: 2px;
  }
</style>
</head>
<body>
<main class="poster">
  <div class="cork"></div>

  <section class="headline-note">
    <span class="tape tape--tl"></span>
    <span class="tape tape--tr"></span>
    <span class="tape tape--bl"></span>
    <span class="tape tape--br"></span>
    <h1 class="headline">Get Your<br>Employees Certified</h1>
  </section>

  <article class="certificate">
    <div class="certificate__frame">
      <p class="certificate__school">CREST Academy</p>
      <p class="certificate__title">Graduation Certification</p>
      <p class="certificate__name">Jordan Avery Lane</p>
      <p class="certificate__body">This document confirms that the learner named above has fully completed the CREST Academy</p>
      <p class="certificate__course">Thrive On The Job</p>
      <p class="certificate__body certificate__body--main">Online Workplace Skills Program with a perfect final score and is recognized as a CREST Academy Graduate with every honor and standing that comes with it. In recognition of this, the present certificate is issued by the faculty at www.crestacademy.example on the advice of the CREST Academy instructors as a result of this learner's coursework.</p>
      <div class="certificate__seal"></div>
      <p class="certificate__date">Date of Graduation</p>
    </div>
  </article>

  <span class="pin" style="left:173px; top:346px;"></span>
  <span class="pin" style="left:724px; top:360px;"></span>

  <figure class="photo-print">
    <div class="photo-print__image" role="img" aria-label="Snapshot of a group of smiling young graduates"></div>
  </figure>
  <span class="pin" style="left:258px; top:606px;"></span>

  <aside class="sticky-note">
    <p class="sticky-note__text">Ask us<br>about a<br>Sneak Peek!</p>
  </aside>

  <aside class="lined-paper">
    <svg width="520" height="280" viewBox="0 0 520 280">
      <path d="M0 0 H520 V262 L505 270 L490 258 L470 272 L450 260 L430 274 L410 262 L388 276 L366 262 L344 272 L322 260 L300 274 L278 262 L256 276 L234 262 L212 272 L190 258 L168 274 L146 262 L124 276 L102 262 L80 272 L58 260 L36 274 L18 262 L0 270 Z" fill="#f6f6f2"/>
      <g stroke="#a9c3dd" stroke-width="1">
        <line x1="0" y1="40" x2="520" y2="40"/>
        <line x1="0" y1="70" x2="520" y2="70"/>
        <line x1="0" y1="100" x2="520" y2="100"/>
        <line x1="0" y1="130" x2="520" y2="130"/>
        <line x1="0" y1="160" x2="520" y2="160"/>
        <line x1="0" y1="190" x2="520" y2="190"/>
        <line x1="0" y1="220" x2="520" y2="220"/>
        <line x1="0" y1="250" x2="520" y2="250"/>
      </g>
      <line x1="44" y1="0" x2="44" y2="265" stroke="#e4a0a0" stroke-width="1.5"/>
      <circle cx="20" cy="60" r="8" fill="#c08a55"/>
      <circle cx="20" cy="150" r="8" fill="#c08a55"/>
      <circle cx="20" cy="240" r="8" fill="#c08a55"/>
    </svg>
    <p class="lined-paper__text">AT A PRICE<br>YOU CANNOT<br>PASS UP !</p>
  </aside>
</main>
</body>
</html>
```